Marlow Realty Real Estate Brokerage Recruiting Flyer

We are a real estate brokerage looking to hire more real estate agents. We need to list everything we have to offer as a company so real estate agents will join our company. this is our company website: www.Marlowrealty.example .

100% COMMISSION NO MONTHLY FEE
$450 Flat Transaction FEE

What We Offer:
24/7 Office Access
Free E & O Insurance for 1st Year
Free Online CE and PLE
Free 1,000 Business Cards
Free Professional Social Media Marketing
Free Printing, Scanning, and Copies
Free Buyer and Seller Presentation Packages
Free Filquay Cloud Based Document Management Access
Access to our Internal Brokerage Forum
Company Profit Sharing!
Private Offices Available to Rent

*Lead Generation Software with over 3,000 Leads
*10 Leads to Start
* Free Personal CRM and Website
*Restrictions and Rules apply

Company Address:
4817 Amberfield Road
Suite 512
Fairfax, VA 22194
Phone: 703-555-0147
email: info@marlowrealty.example

Target Market(s)

Real Estate Agents

Industry/Entity Type

Real Estate

Colors
0555a3
ffffff

Requirements
Must have
• 100% COMMISSION NO MONTHLY FEE
$450 Flat Transaction FEE

What We Offer:
24/7 Office Access
Free Online CE and PLE
Free 1,000 Business Cards
Company Profit Sharing!

*10 Leads to Start

Company Address:
4817 Amberfield Road
Suite 512
Fairfax, VA 22194
Phone: 703-555-0147

```html
<!DOCTYPE html>
<html lang="en">
<head>
<meta charset="utf-8">
<title>Marlow Realty – We Are Hiring</title>
<link rel="stylesheet" href="https://fonts.googleapis.com/css2?family=Montserrat:wght@400;500;600;700;800;900&display=swap">
<style>
  :root{
    --brand-blue:#0a3a86;
    --brand-blue-deep:#062f73;
    --ink:#1c1c1c;
    --white:#ffffff;
    --panel-grey:#e2e2e2;
    --rule-grey:#b9bcbf;
    --stage:#dfe3e0;
    --shadow-grey:#b3b3b3;
    --photo-light:#eef0f3;
    --photo-mid:#cfd6e0;
  }
  *{box-sizing:border-box;margin:0;padding:0}
  html,body{width:1200px;height:2400px;overflow:hidden}
  body{background:var(--stage);font-family:'Montserrat',Arial,sans-serif;position:relative}
  .flyer{
    position:absolute;left:75px;top:439px;width:720px;height:1015px;
    transform:scale(1.5);transform-origin:0 0;
    background:var(--white);overflow:hidden;
    box-shadow:-15px 15px 0 var(--shadow-grey);
  }
  .flyer-art{position:absolute;inset:0}
  .brand{position:absolute;left:62px;top:100px;display:flex;align-items:center;gap:12px}
  .brand-mark{width:30px;height:30px;background:var(--brand-blue)}
  .brand-name{font-family:'Montserrat',Arial,sans-serif;font-weight:600;font-size:34px;color:var(--brand-blue);letter-spacing:1px}
  .headline-kicker{position:absolute;left:50px;top:292px;font-weight:800;font-size:42px;color:var(--ink);letter-spacing:1px}
  .headline-main{position:absolute;left:46px;top:328px;font-weight:900;font-size:96px;line-height:1;color:var(--brand-blue);letter-spacing:1px}
  .role-band{position:absolute;left:42px;top:423px;width:400px;height:48px;background:var(--brand-blue);border-radius:10px 0 0 10px;color:var(--white);font-weight:800;font-size:30px;line-height:48px;padding-left:13px;letter-spacing:1px;white-space:nowrap}
  .terms{position:absolute;left:50px;top:488px;font-weight:800;font-size:31px;line-height:39px;color:var(--ink);letter-spacing:.5px}
  .fee-pill{position:absolute;left:35px;top:584px;width:380px;height:80px;background:var(--brand-blue);border-radius:22px 0 0 22px;color:var(--white);font-weight:900;font-size:26px;line-height:31px;padding:10px 0 0 30px;letter-spacing:.5px}
  .offer-panel{position:absolute;left:392px;top:560px;width:318px;height:455px;background:var(--panel-grey);border-radius:30px 30px 0 0;padding:33px 0 0 20px}
  .offer-title{font-weight:800;font-size:18px;color:var(--brand-blue);letter-spacing:.5px;margin-bottom:13px}
  .offer-list{list-style:none}
  .offer-item{display:flex;align-items:flex-start;gap:9px;font-size:11.3px;line-height:13px;color:var(--ink);min-height:25.5px}
  .offer-item b{font-weight:700}
  .offer-icon{flex:none;width:16px;height:16px;margin-top:-2px}
  .offer-item.two-line{min-height:38px}
  .fine-print{margin-top:2px;display:flex;flex-direction:column;align-items:center;gap:3px;padding-right:20px}
  .fine-print span{font-size:9.5px;line-height:12px;border:1px solid var(--rule-grey);padding:0 8px;color:var(--ink)}
  .contact{position:absolute;left:75px;top:862px;color:var(--white);font-size:13.3px;line-height:15px}
  .contact-row{display:flex;align-items:flex-start;gap:9px;margin-bottom:6px}
  .contact-icon{flex:none;width:16px;height:16px}
  .licence{font-size:10.5px;margin-top:8px}
</style>
</head>
<body>
<div class="flyer">
  <svg class="flyer-art" viewBox="0 0 720 1015" width="720" height="1015" aria-hidden="false">
    <defs>
      <linearGradient id="officeTone" x1="0" y1="0" x2="1" y2="1">
        <stop offset="0" stop-color="#f3f1ef"/>
        <stop offset=".6" stop-color="#e6e8ec"/>
        <stop offset="1" stop-color="#c7ccd3"/>
      </linearGradient>
      <linearGradient id="agentTone" x1="0" y1="0" x2="0" y2="1">
        <stop offset="0" stop-color="#e9dccb"/>
        <stop offset=".45" stop-color="#d8c8b5"/>
        <stop offset="1" stop-color="#2b2b30"/>
      </linearGradient>
    </defs>
    <!-- roofline stripes -->
    <polygon points="350,75 440,0 462,0 372,82 372,250 350,250" fill="#c7c9cc"/>
    <polygon points="372,82 462,0 488,0 392,86 392,250 372,250" fill="var(--brand-blue)"/>
    <g role="img" aria-label="Photo of a handshake over a desk with a model house, keys and a calculator">
      <polygon points="392,86 488,0 720,0 720,290 392,245" fill="url(#officeTone)"/>
    </g>
    <!-- swoosh under photo -->
    <path d="M0,258 Q220,232 392,236 L720,250 L720,262 Q520,248 392,248 Q200,246 0,262 Z" fill="var(--brand-blue)"/>
    <path d="M392,248 Q560,250 720,262 L720,325 Q600,280 392,262 Z" fill="var(--brand-blue)"/>
    <!-- bottom band -->
    <path d="M0,772 L78,818 Q380,735 720,712 L720,1015 L0,1015 Z" fill="var(--brand-blue-deep)"/>
    <path d="M0,762 L78,806 Q380,725 720,702 L720,712 Q380,735 78,818 L0,772 Z" fill="#d5d8dc"/>
    <g role="img" aria-label="Photo of a smiling real estate agent in glasses holding a model house and a folder">
      <path d="M470,560 L470,330 Q475,215 560,215 Q650,215 660,330 L690,560 Z" fill="url(#agentTone)"/>
    </g>
  </svg>

  <div class="brand">
    <span class="brand-mark"></span>
    <span class="brand-name">Marlow Realty</span>
  </div>

  <div class="headline-kicker">WE ARE</div>
  <div class="headline-main">HIRING</div>
  <div class="role-band">REAL ESTATE AGENTS</div>
  <div class="terms">100% COMMISSION<br>NO MONTHLY FEE</div>
  <div class="fee-pill">$450 FLAT<br>TRANSACTION FEE</div>

  <section class="offer-panel">
    <h2 class="offer-title">WHAT WE OFFER:</h2>
    <ul class="offer-list">
      <li class="offer-item"><svg class="offer-icon" viewBox="0 0 16 16"><circle cx="8" cy="8" r="6.5" fill="none" stroke="var(--brand-blue)" stroke-width="1.6"/><path d="M8 4v4l3 2" fill="none" stroke="var(--brand-blue)" stroke-width="1.6"/></svg><span><b>24/7</b> Office Access</span></li>
      <li class="offer-item"><svg class="offer-icon" viewBox="0 0 16 16"><rect x="2.5" y="1.5" width="11" height="13" rx="1" fill="none" stroke="var(--brand-blue)" stroke-width="1.4"/><path d="M5 5h6M5 8h6M5 11h4" stroke="var(--brand-blue)" stroke-width="1.2"/></svg><span><b>Free E &amp; O</b> Insurance for 1st Year</span></li>
      <li class="offer-item"><svg class="offer-icon" viewBox="0 0 16 16"><rect x="1.5" y="3" width="13" height="9" rx="1" fill="none" stroke="var(--brand-blue)" stroke-width="1.4"/><path d="M5 14.5h6" stroke="var(--brand-blue)" stroke-width="1.4"/></svg><span><b>Free Online</b> CE and PLE</span></li>
      <li class="offer-item"><svg class="offer-icon" viewBox="0 0 16 16"><rect x="1.5" y="4" width="13" height="8.5" rx="1" fill="none" stroke="var(--brand-blue)" stroke-width="1.4"/><path d="M4 7h5M4 9.5h3" stroke="var(--brand-blue)" stroke-width="1.2"/></svg><span><b>Free 1,000</b> Business Cards</span></li>
      <li class="offer-item"><svg class="offer-icon" viewBox="0 0 16 16"><rect x="2" y="2" width="12" height="12" rx="2" fill="none" stroke="var(--brand-blue)" stroke-width="1.4"/><circle cx="8" cy="8" r="2.5" fill="var(--brand-blue)"/></svg><span><b>Free Professional</b> Social Media Marketing</span></li>
      <li class="offer-item"><svg class="offer-icon" viewBox="0 0 16 16"><rect x="1.5" y="6" width="13" height="6" rx="1" fill="none" stroke="var(--brand-blue)" stroke-width="1.4"/><path d="M4 6V2h8v4M4 10h8v4H4z" fill="none" stroke="var(--brand-blue)" stroke-width="1.3"/></svg><span><b>Free Printing</b>, Scanning, and Copies</span></li>
      <li class="offer-item"><svg class="offer-icon" viewBox="0 0 16 16"><rect x="1.5" y="2" width="13" height="10" rx="1" fill="none" stroke="var(--brand-blue)" stroke-width="1.4"/><path d="M8 12v3M5 15h6M4 9l3-3 2 2 3-3" fill="none" stroke="var(--brand-blue)" stroke-width="1.2"/></svg><span><b>Free Buyer</b> and Seller Presentation Packages</span></li>
      <li class="offer-item two-line"><svg class="offer-icon" viewBox="0 0 16 16"><path d="M4.5 12.5a3 3 0 0 1 0-6 4 4 0 0 1 7.5-1 3.5 3.5 0 0 1 0 7z" fill="none" stroke="var(--brand-blue)" stroke-width="1.4"/></svg><span><b>Free Filquay</b> Cloud Based Document<br>Management Access</span></li>
      <li class="offer-item"><svg class="offer-icon" viewBox="0 0 16 16"><circle cx="5" cy="5" r="2.3" fill="none" stroke="var(--brand-blue)" stroke-width="1.3"/><circle cx="11" cy="5" r="2.3" fill="none" stroke="var(--brand-blue)" stroke-width="1.3"/><path d="M1.5 13a3.5 3.5 0 0 1 7 0M7.5 13a3.5 3.5 0 0 1 7 0" fill="none" stroke="var(--brand-blue)" stroke-width="1.3"/></svg><span><b>Access</b> to our Internal Brokerage Forum</span></li>
      <li class="offer-item"><svg class="offer-icon" viewBox="0 0 16 16"><path d="M2 14h12M4 14V9M8 14V5M12 14V2" stroke="var(--brand-blue)" stroke-width="1.8"/></svg><span><b>Company Profit</b> Sharing!</span></li>
      <li class="offer-item"><svg class="offer-icon" viewBox="0 0 16 16"><rect x="1.5" y="7" width="9" height="7" fill="none" stroke="var(--brand-blue)" stroke-width="1.3"/><path d="M1.5 7 6 3l4.5 4" fill="none" stroke="var(--brand-blue)" stroke-width="1.3"/><circle cx="12.5" cy="9" r="2" fill="var(--brand-blue)"/></svg><span><b>Private Offices</b> Available to Rent</span></li>
    </ul>
    <div class="fine-print">
      <span>*Lead Generation Software with over 3,000 Leads</span>
      <span>*10 Leads to Start</span>
      <span>* Free Personal CRM and Website</span>
      <span>*Restrictions and Rules apply</span>
    </div>
  </section>

  <address class="contact" style="font-style:normal">
    <div class="contact-row"><svg class="contact-icon" viewBox="0 0 16 16"><circle cx="8" cy="8" r="7.5" fill="var(--white)"/><path d="M8 3.2a3 3 0 0 0-3 3c0 2.3 3 6 3 6s3-3.7 3-6a3 3 0 0 0-3-3z" fill="var(--brand-blue)"/><circle cx="8" cy="6.2" r="1.1" fill="var(--white)"/></svg><span>4817 Amberfield Road<br>Suite 512, Fairfax, VA 22194</span></div>
    <div class="contact-row"><svg class="contact-icon" viewBox="0 0 16 16"><circle cx="8" cy="8" r="7.5" fill="var(--white)"/><path d="M5 4l1.7-.4 1 2.3-1 .8a6 6 0 0 0 2.6 2.6l.8-1 2.3 1L12 11c-4 .4-7.4-3-7-7z" fill="var(--brand-blue)"/></svg><span>703-555-0147</span></div>
    <div class="contact-row"><svg class="contact-icon" viewBox="0 0 16 16"><circle cx="8" cy="8" r="7.5" fill="var(--white)"/><rect x="3.8" y="5" width="8.4" height="6" fill="none" stroke="var(--brand-blue)" stroke-width="1.2"/><path d="M3.8 5 8 8.5 12.2 5" fill="none" stroke="var(--brand-blue)" stroke-width="1.2"/></svg><span>info@marlowrealty.example</span></div>
    <div class="contact-row"><svg class="contact-icon" viewBox="0 0 16 16"><circle cx="8" cy="8" r="7.5" fill="var(--white)"/><circle cx="8" cy="8" r="4.5" fill="none" stroke="var(--brand-blue)" stroke-width="1.1"/><path d="M3.5 8h9M8 3.5c-2.4 2.6-2.4 6.4 0 9M8 3.5c2.4 2.6 2.4 6.4 0 9" fill="none" stroke="var(--brand-blue)" stroke-width="1"/></svg><span>www.Marlowrealty.example</span></div>
    <div class="licence">Licensed in D.C., Maryland, and Virginia</div>
  </address>
</div>
</body>
</html>
```